ZN Banner Ad for campaign for mobile app

It's a Bolt 2 Pup ZN advertisement at 1:1, 16:9, and 1.91:1 aspect ratios. The advertisement will be on mobile devices on VendOS. Text must be less than 20% of the screen.

https://apps.vendora.example/us/app/chatty-bolt-pup-2/id804261975

```html
<!DOCTYPE html>
<html lang="en">
<head>
<meta charset="utf-8">
<title>Bolt2Pup ZN Banner Set</title>
<link rel="stylesheet" href="https://fonts.googleapis.com/css2?family=Inter:wght@300;700&family=Inter+Tight:wght@600;700;800&display=swap">
<style>
:root{
  --board:#adc4d1;
  --label:#1d3a4e;
  --white:#ffffff;
  --black:#0b0b0f;
  --navy:#14093f;
  --purple:#a52fe0;
  --pink:#f0338f;
  --orange:#f7932a;
  --yellow:#f4c531;
  --blue:#2f6bd8;
  --teal:#17a6c9;
  --frame:#2a2a33;
  --rim:#b9b6cf;
}
*{box-sizing:border-box;margin:0;padding:0}
html,body{width:735px;height:1200px;overflow:hidden}
body{background:var(--board);position:relative;font-family:"Inter Tight",Arial,sans-serif}

.size-label{position:absolute;left:73px;font-family:"Inter",Arial,sans-serif;font-weight:300;color:var(--label);font-size:23px;line-height:28px;letter-spacing:-0.5px}
.size-label b{font-weight:700}

.banner{position:absolute;overflow:hidden;box-shadow:0 8px 18px rgba(20,40,60,.28)}
.banner-portrait{left:226px;top:76px;width:217px;height:386px;
  background:
    radial-gradient(circle at 100% 28%,var(--yellow) 0 22px,transparent 23px),
    radial-gradient(ellipse 60% 40% at 0% 30%,rgba(190,220,60,.85),transparent 70%),
    radial-gradient(ellipse 80% 50% at 100% 75%,rgba(100,60,230,.9),transparent 70%),
    linear-gradient(165deg,#3a1450 0%,#b8284f 18%,var(--orange) 35%,var(--pink) 62%,#9b2ee0 100%)}
.banner-square{left:226px;top:509px;width:348px;height:348px;
  background:
    radial-gradient(ellipse 70% 35% at 30% 95%,rgba(247,120,60,.95),transparent 70%),
    radial-gradient(ellipse 60% 40% at 95% 80%,rgba(190,40,220,.9),transparent 70%),
    radial-gradient(ellipse 50% 30% at 35% 62%,rgba(60,110,230,.8),transparent 70%),
    linear-gradient(180deg,#0c0535 0%,var(--navy) 45%,#3a1a7a 65%,var(--pink) 85%,#f05a6a 100%)}
.banner-wide{left:226px;top:903px;width:425px;height:222px;
  background:
    radial-gradient(ellipse 45% 60% at 8% 85%,rgba(23,166,201,.85),transparent 70%),
    radial-gradient(ellipse 50% 60% at 100% 100%,rgba(190,30,210,.95),transparent 70%),
    linear-gradient(170deg,#050510 0%,#0d0a2a 40%,#2a2a8a 70%,#7a2ad0 100%)}

.title{position:absolute;color:var(--white);font-weight:800;letter-spacing:-1.5px}
.title-portrait{left:0;right:0;top:26px;text-align:center;font-size:29px;line-height:30px}
.rule{position:absolute;height:1px;background:rgba(255,255,255,.45)}
.tagline{position:absolute;color:var(--white);font-weight:700;letter-spacing:-.6px}
.tagline-portrait{left:0;right:0;top:70px;text-align:center;font-size:16px;line-height:16px}

.stack-title{position:absolute;color:var(--white);font-weight:800;letter-spacing:-2px}
.stack-title .two{position:absolute;color:var(--purple);font-weight:700}

.store-badge{position:absolute;display:flex;align-items:center;justify-content:center;gap:6px;padding:0 7px;border-radius:5px;background:var(--black);border:1px solid #8a8a8a;color:var(--white);white-space:nowrap}
.store-badge .dot{width:9px;height:9px;border-radius:50%;background:var(--white);flex:none}
.store-badge .copy{display:flex;flex-direction:column;justify-content:center}
.store-badge .small{display:block;font-size:6px;line-height:8px;font-weight:600;letter-spacing:.3px}
.store-badge .big{display:block;font-size:11.5px;line-height:12px;font-weight:600;letter-spacing:-.1px}
.store-badge.light{background:var(--white);color:#222;border:none;border-radius:15px;box-shadow:0 2px 6px rgba(0,0,0,.25)}
.store-badge.light .dot{background:#222}

.phone{position:absolute;border-radius:14px;background:var(--frame);border:2px solid var(--rim);padding:4px;box-shadow:0 6px 12px rgba(0,0,0,.3)}
.phone .screen{width:100%;height:100%;border-radius:10px;overflow:hidden;position:relative;background:var(--black)}
.phone .shot{position:absolute;left:0;right:0;top:14%;bottom:8%;background:linear-gradient(180deg,#7a4a2a 0%,#a8754a 45%,#c8a070 75%,#e5d3a8 100%)}
.phone .island{position:absolute;top:3%;left:34%;width:32%;height:4%;border-radius:6px;background:#000}

.app-icon{position:absolute;left:25px;top:30px;width:73px;height:73px;border-radius:17px;background:radial-gradient(circle at 50% 60%,#f2efea 0 40%,#8a5a3a 70%,#d9d4cc 100%)}
</style>
</head>
<body>

<div class="size-label" style="top:206px">Bolt2Pup<br>Post <b>16:9</b></div>
<div class="size-label" style="top:643px">Bolt2Pup<br>Post <b>1:1</b></div>
<div class="size-label" style="top:984px">Bolt2Pup<br>Post <b>1.91:1</b></div>

<!-- Portrait banner -->
<section class="banner banner-portrait">
  <h2 class="title title-portrait">Bolt2Pup</h2>
  <div class="rule" style="left:40px;right:40px;top:63px"></div>
  <p class="tagline tagline-portrait">Get amused and<br>occupied for hours!</p>
  <a class="store-badge" style="left:52px;top:110px;width:114px;height:31px">
    <span class="dot"></span><span class="copy"><span class="small">Download on the</span><span class="big">Vendora Store</span></span>
  </a>
  <div class="phone" style="left:22px;top:176px;width:85px;height:197px;transform:rotate(-2deg)">
    <div class="screen"><div class="island"></div><div class="shot" role="img" aria-label="App screenshot: the cartoon pup in a kitchen"></div></div>
  </div>
  <div class="phone" style="left:110px;top:147px;width:85px;height:197px;transform:rotate(2deg)">
    <div class="screen"><div class="island"></div><div class="shot" role="img" aria-label="App screenshot: the cartoon pup in a bathroom"></div></div>
  </div>
</section>

<!-- Square banner -->
<section class="banner banner-square">
  <div class="app-icon" role="img" aria-label="App icon with the cartoon pup character"></div>
  <h2 class="stack-title" style="left:24px;top:117px;font-size:44px;line-height:39px">Bolt<br>Pup<span class="two" style="left:84px;top:-10px;font-size:64px;line-height:64px">2</span></h2>
  <div class="rule" style="left:25px;width:121px;top:205px"></div>
  <p class="tagline" style="left:25px;top:218px;font-size:17px;line-height:19px">Bolt Brings the<br>Funny to VendOS</p>
  <a class="store-badge light" style="left:25px;top:269px;width:108px;height:29px">
    <span class="dot"></span><span class="copy"><span class="small">DOWNLOAD ON THE</span><span class="big">Vendora Store</span></span>
  </a>
  <div class="phone" style="left:179px;top:27px;width:142px;height:294px;border-radius:22px">
    <div class="screen" style="border-radius:18px"><div class="island"></div><div class="shot" role="img" aria-label="App screenshot: the cartoon pup waving in a kitchen"></div></div>
  </div>
</section>

<!-- Wide banner -->
<section class="banner banner-wide">
  <h2 class="stack-title" style="left:27px;top:26px;font-size:41px;line-height:37px">Bolt<br>Pup<span class="two" style="left:80px;top:-10px;font-size:60px;line-height:60px">2</span></h2>
  <p class="tagline" style="left:28px;top:122px;font-size:18px;line-height:18px;letter-spacing:-.8px">Record your own<br>sessions with Bolt!</p>
  <a class="store-badge" style="left:29px;top:169px;width:108px;height:28px">
    <span class="dot"></span><span class="copy"><span class="small">Download on the</span><span class="big">Vendora Store</span></span>
  </a>
  <div class="phone" style="left:203px;top:15px;width:69px;height:161px;transform:rotate(-3deg)">
    <div class="screen"><div class="island"></div><div class="shot" role="img" aria-label="App screenshot: the cartoon pup in a bathtub"></div></div>
  </div>
  <div class="phone" style="left:322px;top:20px;width:70px;height:162px;transform:rotate(3deg)">
    <div class="screen"><div class="island"></div><div class="shot" role="img" aria-label="App screenshot: the cartoon pup lying in a kitchen"></div></div>
  </div>
  <div class="phone" style="left:262px;top:50px;width:76px;height:158px">
    <div class="screen"><div class="island"></div><div class="shot" role="img" aria-label="App screenshot: the cartoon pup in a bathroom"></div></div>
  </div>
</section>

</body>
</html>
```